New business card for civil engineering company - "Keystone Audit"

We need a business card designed for our new structural engineering company.

The company name is "Keystone Audit" logo files attached.

We would like the following:
* Two-sided card
* Simple design

Information to be placed on the card:
Name - Marcus Dellow
Job Title - Director / Structural Engineer
Credentials - BEng(Hons), CPEng, CMengNZ, IntPE(NZ)
Email - marcus.dellow@keystoneaudit.co.nz
mobile - 0219364058
website - www.keystoneaudit.co.nz

```html
<!DOCTYPE html>
<html lang="en">
<head>
<meta charset="utf-8">
<title>Keystone Audit — Business Card</title>
<link rel="stylesheet" href="https://fonts.googleapis.com/css2?family=Bodoni+Moda:opsz,wght@6..96,400&family=Playfair+Display:wght@700&display=swap">
<style>
  :root {
    --card-blue: #032d93;
    --panel-tint: #06319a;
    --divider: #e8ecf7;
    --ink-light: #ffffff;
    --ink-soft: #f1f3fa;
  }
  html, body {
    margin: 0;
    padding: 0;
    width: 1200px;
    height: 777px;
    overflow: hidden;
    background: var(--card-blue);
  }
  .card {
    position: relative;
    width: 1200px;
    height: 777px;
    background: var(--card-blue);
    overflow: hidden;
  }
  .brand-face {
    position: absolute;
    left: 0;
    top: 0;
    width: 556px;
    height: 777px;
  }
  .brand-name {
    position: absolute;
    left: 0;
    top: 540px;
    width: 556px;
    display: flex;
    justify-content: center;
    align-items: center;
    gap: 16px;
    font-family: "Bodoni Moda", serif;
    font-weight: 400;
    font-size: 46px;
    line-height: 1;
    color: var(--ink-light);
  }
  .brand-mark {
    width: 28px;
    height: 28px;
    background: var(--ink-light);
  }
  .face-divider {
    position: absolute;
    left: 555px;
    top: 0;
    width: 4px;
    height: 777px;
    background: var(--divider);
  }
  .contact-face {
    position: absolute;
    left: 559px;
    top: 0;
    width: 641px;
    height: 777px;
  }
  .backdrop-pattern {
    position: absolute;
    inset: 0;
    background: var(--panel-tint);
  }
  .person-name {
    position: absolute;
    left: 87px;
    top: 104px;
    margin: 0;
    font-family: "Playfair Display", serif;
    font-weight: 700;
    font-size: 60px;
    line-height: 1;
    color: var(--ink-light);
    letter-spacing: -0.5px;
  }
  .person-role,
  .person-credentials {
    position: absolute;
    left: 87px;
    margin: 0;
    font-family: "Bodoni Moda", serif;
    font-weight: 400;
    font-size: 23px;
    line-height: 1;
    color: var(--ink-soft);
  }
  .person-role { top: 218px; }
  .person-credentials { top: 279px; }
  .contact-list {
    position: absolute;
    left: 87px;
    top: 460px;
    margin: 0;
    padding: 0;
    list-style: none;
  }
  .contact-item {
    display: flex;
    align-items: center;
    height: 54px;
    margin-bottom: 25px;
    font-family: "Bodoni Moda", serif;
    font-weight: 400;
    font-size: 24px;
    color: var(--ink-light);
  }
  .contact-icon {
    width: 54px;
    height: 54px;
    flex: none;
    margin-right: 37px;
  }
</style>
</head>
<body>
<main class="card">
  <section class="brand-face">
    <div class="brand-name"><span class="brand-mark"></span>Keystone Audit</div>
  </section>

  <div class="face-divider"></div>

  <section class="contact-face">
    <div class="backdrop-pattern" role="img" aria-label="Faint repeating brand pattern in deep blue"></div>

    <h1 class="person-name">Marcus Dellow</h1>
    <p class="person-role">Director / Structural Engineer</p>
    <p class="person-credentials">BEng(Hons), CPEng, CMengNZ, IntPE(NZ)</p>

    <ul class="contact-list">
      <li class="contact-item">
        <svg class="contact-icon" viewBox="0 0 54 54" aria-hidden="true">
          <rect x="1" y="11" width="52" height="33" fill="#fff"/>
          <path d="M2 12 L27 32 L52 12" fill="none" stroke="#032d93" stroke-width="2.5"/>
          <path d="M2 43 L21 27 M52 43 L33 27" fill="none" stroke="#032d93" stroke-width="2.5"/>
        </svg>
        marcus.dellow@keystoneaudit.co.nz
      </li>
      <li class="contact-item">
        <svg class="contact-icon" viewBox="0 0 54 54" aria-hidden="true">
          <path fill="#fff" d="M14 3c2-1 4 0 5 2l5 9c1 2 0 4-1 5l-4 3c2 6 7 12 13 15l3-4c1-2 3-2 5-1l9 5c2 1 3 3 2 5l-3 6c-2 3-5 4-9 3C22 46 8 32 3 15c-1-4 0-7 3-9z"/>
        </svg>
        0219364058
      </li>
      <li class="contact-item">
        <svg class="contact-icon" viewBox="0 0 54 54" aria-hidden="true">
          <g fill="none" stroke="#fff" stroke-width="4">
            <circle cx="27" cy="27" r="23"/>
            <ellipse cx="27" cy="27" rx="10" ry="23"/>
            <line x1="27" y1="4" x2="27" y2="50"/>
            <line x1="4" y1="27" x2="50" y2="27"/>
            <path d="M8 15 H46 M8 39 H46"/>
          </g>
        </svg>
        www.keystoneaudit.co.nz
      </li>
    </ul>
  </section>
</main>
</body>
</html>
```